Verpackungen für drei Naturheilprodukte und ein Verkaufsdisplay
Zielgruppe
Wir sind ein Team von drei Personen die sich das Ziel gesetzt haben möglichst viele Personen mit den Wirkstoffen aus der Natur zu erreichen. Wir sind der Überzeugung, dass die Wirkstoffe der Natur vorbeugend schlimmeres verhindern kann und auch auf sanfte Art und Weise dem Körber die Natürliche Energie zurückgeben kann.
Die Produkte werden laufend erweitert somit wird auch auf eine zukünftige Zusammenarbeit Wert gelegt.
Momentan arbeiten wir an folgenden Produkten die verpackt werden müssen:
- Bachblüten/CBD Globuli:
Diese wirken beruhigend, angstlösend stresslindernd. Die Verpackung wird aus einem Faltkarton sein (40mm x 35mm x 80mm)
- Hautpflege Salbe
Diese ist auch auf CBD und Kamillenblüten Basis. Diese wirkt entzündungshemmend, beschleunigt und unterstützt den Heilungsprozess. Die Creme ist in einem 30ml Glass.
- CBD Blüten (legales Cannabis).
Dies wirkt besonders Schmerzlindernd, krampflösend und entzündungshemmend. Die momentan verkaufte Sorte der Hanfblüte ist CBD Velvet ca. 16% CBD/0,6% Gehalt THC (diese Angaben sollten einfach zu wechseln sein). Die Verpackung wird aus einem Faltkarton sein (ca. 60mm x 50mm x 80mm, für andere Vorschläge offen).
- Weiter stelle ich mir ein Ausstellungsdisplay vor. So Kompakt wie möglich, damit es gut auf dem Verkaufstresen platzfindet, jedoch trotzdem ins Auge sticht.
Aufgabenstellung
Sie Designen hier unsere Produktelinie momentan bestehend aus drei Produkten. Diese sollten ein einheitliches erscheinen und ein edles und schlichtes auftreten haben. Nicht Hanflastig. Das Hauptaugenmerk sollte eher auf Wellness, Gesundheit und Natur gesetzt sein. Den Rest lasse ich mich auf die Kreativität der Designer überraschen

```html
<!DOCTYPE html>
<html lang="de">
<head>
<meta charset="utf-8">
<title>Bachblüten CBD Globuli – Faltschachtel</title>
<link rel="stylesheet" href="https://fonts.googleapis.com/css2?family=Poiret+One&display=swap">
<style>
  :root {
    --page: #ffffff;
    --kraft: #ab8660;
    --kraft-light: #b89470;
    --leaf: #8fd45a;
    --ink: #ffffff;
  }
  * { margin: 0; padding: 0; box-sizing: border-box; }
  html, body { width: 851px; height: 1200px; overflow: hidden; background: var(--page); }
  .canvas { position: relative; width: 851px; height: 1200px; }
  .box-front {
    position: absolute; left: 122px; top: 44px; width: 552px; height: 1062px;
    background: linear-gradient(160deg, var(--kraft-light), var(--kraft));
    overflow: hidden;
  }
  .box-front svg.green-base { position: absolute; inset: 0; }
  .label { position: absolute; left: 0; width: 100%; text-align: center;
    font-family: "Poiret One", sans-serif; color: var(--ink); }
  .product-title { top: 88px; font-size: 66px; letter-spacing: 3px; }
  .product-type { top: 172px; font-size: 54px; letter-spacing: 4px; }
  .rule { position: absolute; top: 280px; left: 60px; width: 432px; height: 2px; background: var(--ink); }
  .content-size { top: 306px; font-size: 24px; letter-spacing: 3px; }
  .brand { position: absolute; top: 372px; left: 0; width: 100%;
    display: flex; flex-direction: column; align-items: center; gap: 12px; }
  .brand-dot { width: 100px; height: 100px; border: 3px solid var(--ink); border-radius: 50%; }
  .brand-name { font-family: "Poiret One", sans-serif; color: var(--ink); font-size: 26px; letter-spacing: 2px; }
  .claim { top: 578px; font-size: 40px; letter-spacing: 2px; }
</style>
</head>
<body>
<div class="canvas">
  <div class="box-front">
    <svg class="green-base" width="552" height="1062" viewBox="0 0 552 1062" aria-hidden="true">
      <path d="M0 726 C40 712 70 698 100 700 C150 704 200 748 270 752 C340 756 420 700 552 684 L552 1062 L0 1062 Z" fill="var(--leaf)"/>
    </svg>
    <h1 class="label product-title">BACHBLÜTEN</h1>
    <h2 class="label product-type">CBD GLOBULI</h2>
    <div class="rule"></div>
    <p class="label content-size">004ML E</p>
    <div class="brand">
      <div class="brand-dot"></div>
      <span class="brand-name">CBD Velvet</span>
    </div>
    <p class="label claim">100% NATÜRLICH</p>
  </div>
</div>
</body>
</html>
```